Current Employment Opportunities Email Template

We would like to redesign our internal job listing email template we send out each month. The email service we use is MailChimp and would like the template to be easy to edit when updating job postings. I attached an example below.

Font styles to use
Sans Serif

Colors

Designer to choose colors to be used in the design.

```html
<!DOCTYPE html>
<html lang="en">
<head>
<meta charset="utf-8">
<title>Ridgeway Services – Current Opportunities</title>
<link rel="stylesheet" href="https://fonts.googleapis.com/css2?family=Figtree:wght@300;400;500;600;700;800&display=swap">
<style>
  :root {
    --page-bg: #ececec;
    --card-bg: #ffffff;
    --navy: #1c2b55;
    --pale-blue: #e3ebfb;
    --text-grey: #555a63;
    --muted-grey: #7a7f88;
    --rule: #dcdde0;
    --link-red: #e0262b;
    --accent-gold: #f2b431;
  }
  * { box-sizing: border-box; margin: 0; padding: 0; }
  html, body {
    width: 701px; height: 1200px; overflow: hidden;
    background: var(--page-bg);
    font-family: "Figtree", sans-serif;
  }
  .canvas { position: relative; width: 701px; height: 1200px; }

  .preheader {
    position: absolute; top: 41px; left: 0; width: 100%;
    text-align: center; font-size: 10px; font-weight: 600; color: var(--muted-grey); line-height: 12px;
  }
  .preheader a { color: var(--link-red); text-decoration: underline; }

  .email-card {
    position: absolute; left: 134px; top: 91px; width: 434px; height: 947px;
    background: var(--card-bg); border-radius: 8px; overflow: hidden;
  }

  .brand {
    position: absolute; top: 28px; left: 0; width: 100%; text-align: center;
    color: var(--navy); font-weight: 800;
  }
  .brand-name { font-size: 34px; letter-spacing: 1px; line-height: 34px; display: block; }
  .brand-sub { font-size: 10px; letter-spacing: 1px; line-height: 12px; display: block; margin-left: 110px; }
  .brand-rule { position: absolute; top: 81px; left: 18px; width: 398px; height: 3px; background: var(--rule); }

  .intro { position: absolute; top: 96px; left: 18px; width: 398px; text-align: center; }
  .intro h1 { font-size: 24px; font-weight: 800; color: var(--navy); line-height: 30px; }
  .intro .tagline { font-size: 11.5px; font-weight: 700; color: var(--text-grey); margin-top: 2px; }
  .intro .lead {
    margin-top: 8px; text-align: left; font-size: 12.5px; font-weight: 300;
    color: var(--muted-grey); line-height: 19px;
  }

  .section-banner { position: absolute; top: 262px; left: 0; width: 434px; height: 100px; }
  .banner-label {
    position: absolute; top: 302px; left: 94px; width: 246px; height: 36px;
    text-align: center; font-size: 13.5px; font-weight: 800; color: var(--navy);
    line-height: 36px; letter-spacing: 0.2px;
  }

  .job { position: absolute; left: 0; width: 434px; }
  .job-city {
    position: absolute; font-size: 27px; font-weight: 300; color: var(--navy); letter-spacing: 0.5px;
  }
  .job-divider { position: absolute; width: 3px; background: var(--rule); }
  .job-info { position: absolute; }
  .job-title { font-size: 13.5px; font-weight: 700; color: var(--text-grey); line-height: 17px; }
  .job-location { font-size: 12px; font-weight: 500; color: var(--navy); margin-top: 4px; }
  .job-summary { font-size: 10px; font-weight: 700; color: var(--text-grey); margin-top: 6px; }
  .job-button {
    display: block; width: 206px; height: 30px; margin-top: 11px; border-radius: 15px;
    background: var(--navy); color: #fff; text-align: center; line-height: 30px;
    font-size: 10.5px; font-weight: 500; text-decoration: none;
  }
  .row-rule { position: absolute; left: 18px; width: 398px; height: 2px; background: var(--rule); }

  .footer-edge { position: absolute; left: 0; top: 834px; width: 434px; height: 22px; }
  .footer {
    position: absolute; left: 0; top: 853px; width: 434px; height: 94px; background: var(--navy); color: #fff;
  }
  .footer-contact {
    position: absolute; top: 10px; left: 0; width: 100%; display: flex; justify-content: center; align-items: center; gap: 8px;
    font-size: 11.5px; font-weight: 400;
  }
  .footer-rule { position: absolute; top: 40px; left: 18px; width: 398px; height: 1px; background: rgba(255,255,255,0.25); }
  .copyright { position: absolute; top: 54px; left: 18px; font-size: 10.5px; font-weight: 600; }
  .social { position: absolute; top: 48px; right: 18px; display: flex; gap: 4px; }
  .social span { width: 24px; height: 24px; border: 1.5px solid #fff; border-radius: 50%; display: block; }
</style>
</head>
<body>
<div class="canvas">
  <p class="preheader">Is this email not displaying correctly?<br><a href="#">View it in your browser.</a></p>

  <main class="email-card">
    <div class="brand">
      <span class="brand-name">RIDGEWAY</span>
      <span class="brand-sub">SERVICES INC.</span>
    </div>
    <div class="brand-rule"></div>

    <section class="intro">
      <h1>Today's Talent Oppurtunities</h1>
      <p class="tagline">Want to be a part of the most efficient and elite team in the industry?</p>
      <p class="lead">We've got a list of opportunities here at Ridgeway that we'd love for you to strive for! These openings allow you to fully tuilize your strengths, walk alongside us as we grow exponentially farther than we could ever dream. and leverage your successes to climb your way up the ladder of professional growth and leadership withing our organization!</p>
    </section>

    <svg class="section-banner" viewBox="0 0 434 100" aria-hidden="true">
      <polygon points="0,12 434,0 434,48 0,70" fill="var(--pale-blue)"/>
      <polygon points="0,46 434,60 434,72 0,79" fill="var(--navy)"/>
      <path d="M98 45 H336 Q341 45 341 50 V75 Q341 80 336 80 H230 L217 89 L204 80 H98 Q93 80 93 75 V50 Q93 45 98 45 Z" fill="#fff" stroke="var(--navy)" stroke-width="2"/>
      <circle cx="200" cy="34" r="16" fill="var(--navy)"/>
      <polygon points="192,31 204,25 204,42 192,36" fill="var(--accent-gold)"/>
      <rect x="189" y="31" width="4" height="5" fill="#fff"/>
    </svg>
    <div class="banner-label">CURRENT OPPORTUNITIES</div>

    <article class="job" style="top:379px;height:100px;">
      <span class="job-city" style="left:18px;top:32px;">DALLAS</span>
      <div class="job-divider" style="left:131px;top:0;height:100px;"></div>
      <div class="job-info" style="left:153px;top:4px;">
        <h2 class="job-title">REGIONAL SALES MANGER</h2>
        <p class="job-location">DALLAS,TX</p>
        <p class="job-summary">Restoration Technician in the Dallas/Ft. Worth Area</p>
        <a class="job-button" href="#">Learn More About This Opportunity</a>
      </div>
    </article>
    <div class="row-rule" style="top:495px;"></div>

    <article class="job" style="top:530px;height:100px;">
      <div class="job-info" style="left:18px;top:4px;">
        <h2 class="job-title">JANITORIAL SALES/ACCOUNT MANAGER</h2>
        <p class="job-location">AUSTIN,TX</p>
        <p class="job-summary">Rewarding, fufilling and goal orented position..</p>
        <a class="job-button" href="#">Learn More About This Opportunity</a>
      </div>
      <div class="job-divider" style="left:310px;top:-8px;height:102px;"></div>
      <span class="job-city" style="left:323px;top:31px;">AUSTIN</span>
    </article>
    <div class="row-rule" style="top:646px;"></div>

    <article class="job" style="top:677px;height:100px;">
      <span class="job-city" style="left:18px;top:32px;">DENVER</span>
      <div class="job-divider" style="left:131px;top:0;height:100px;"></div>
      <div class="job-info" style="left:153px;top:4px;">
        <h2 class="job-title">JANITORIAL SALES/ACCOUNT MANGER</h2>
        <p class="job-location">DENVER,CO</p>
        <p class="job-summary">Rewarding, fufilling and goal orented position..</p>
        <a class="job-button" href="#">Learn More About This Opportunity</a>
      </div>
    </article>

    <svg class="footer-edge" viewBox="0 0 434 22" aria-hidden="true">
      <polygon points="0,0 434,12 434,22 0,22" fill="var(--pale-blue)"/>
    </svg>
    <footer class="footer">
      <div class="footer-contact">
        <svg width="22" height="22" viewBox="0 0 22 22" aria-hidden="true">
          <circle cx="11" cy="11" r="11" fill="#fff"/>
          <rect x="5" y="7" width="12" height="8" rx="1" fill="var(--navy)"/>
          <polyline points="5.5,7.5 11,11.5 16.5,7.5" fill="none" stroke="#fff" stroke-width="1.2"/>
        </svg>
        <span>hello@ridgewayjobs.com</span>
      </div>
      <div class="footer-rule"></div>
      <p class="copyright">Copyright © 2018 Your Website - All Rights Reserved.</p>
      <div class="social" aria-label="Social links"><span></span><span></span><span></span><span></span></div>
    </footer>
  </main>
</div>
</body>
</html>
```